Business Card for Kinesiologist Practitioner

I need a logo and business card designing for a Kinesiologist Practitioner. I would like the card to be double sided. The look and feel of the logo and graphics should depict natural healing and well being. I would like a modern, fresh and contemporary design with a professional style. I have attached some logos and business cards that I liek from other natural health practitioners. I have also attached some logos that I like and a mock up of the business card style. Please however use your own creative input to change any element as you feel appropriate.

I have used the strap line "Quiet Renewal" which I would like underneath the logo. For the logo I like natural objects and possibly with 3 elements in the design as the course I have studied follows a "Open Arc " healing concept (mind, body, soul). Maybe a tree or flower with 3 elements and a representation or suggestion of the human body somehow. You will see from the logos i have uploaded

Industry/Entity Type

Business

Contact Information for Business Card

Please see the mock up attached.

Font styles to use
Serif
Sans Serif

Colors
faa54b
acd036
fbee3d
85cae6

Requirements
Must have
• Note the colours are just suggested colours. Please us your own creative licence.

```html
<!DOCTYPE html>
<html lang="en">
<head>
<meta charset="utf-8">
<title>Quiet Renewal – Business Card</title>
<link rel="stylesheet" href="https://fonts.googleapis.com/css2?family=Montserrat:wght@400&family=EB+Garamond:ital,wght@0,400;0,600;1,500&display=swap">
<style>
  :root {
    --backdrop: #2a2a2a;
    --card-orange: #f2963a;
    --card-orange-light: #f7a54e;
    --card-white: #f7f7f7;
    --accent-orange: #e9832f;
    --accent-green: #8dba2a;
    --ink: #2b2b2b;
    --divider: #3a3a3a;
  }
  * { margin: 0; padding: 0; box-sizing: border-box; }
  html, body {
    width: 1200px;
    height: 873px;
    overflow: hidden;
    background: var(--backdrop);
  }
  .canvas {
    width: 1200px;
    height: 873px;
    display: flex;
    align-items: center;
    justify-content: center;
    gap: 60px;
  }
  .card {
    width: 520px;
    height: 300px;
    border-radius: 18px;
    position: relative;
    box-shadow: 0 14px 30px rgba(0,0,0,0.45);
  }
  .card--front {
    background: linear-gradient(160deg, var(--card-orange-light), var(--card-orange));
    display: flex;
    align-items: center;
    justify-content: center;
  }
  .brand {
    display: flex;
    align-items: center;
    gap: 12px;
    font-family: "Montserrat", sans-serif;
    font-weight: 400;
    white-space: nowrap;
  }
  .brand__dot {
    border-radius: 50%;
    flex: none;
  }
  .card--front .brand { font-size: 34px; color: #ffffff; }
  .card--front .brand__dot { width: 30px; height: 30px; background: #ffffff; }

  .card--back {
    background: var(--card-white);
    font-family: "EB Garamond", serif;
    color: var(--ink);
  }
  .card--back .brand {
    position: absolute;
    top: 48px;
    left: 0;
    right: 0;
    justify-content: center;
    font-size: 28px;
    color: var(--accent-orange);
  }
  .card--back .brand__dot { width: 24px; height: 24px; background: var(--accent-orange); }

  .identity {
    position: absolute;
    top: 132px;
    left: 0;
    right: 0;
    display: flex;
    justify-content: center;
    align-items: center;
    gap: 12px;
  }
  .identity__name {
    font-weight: 600;
    font-size: 22px;
    color: var(--accent-orange);
  }
  .identity__creds { font-size: 14px; margin-left: -4px; }
  .identity__rule {
    width: 1px;
    height: 30px;
    background: var(--divider);
  }
  .identity__role {
    font-style: italic;
    font-weight: 500;
    font-size: 16px;
    color: var(--accent-green);
  }
  .contacts {
    position: absolute;
    bottom: 52px;
    left: 0;
    right: 0;
    display: flex;
    justify-content: center;
    gap: 40px;
    font-size: 17px;
  }
  .contact {
    display: flex;
    align-items: center;
    gap: 8px;
  }
  .contact__icon { width: 22px; height: 22px; flex: none; }
</style>
</head>
<body>
<main class="canvas">
  <section class="card card--front" aria-label="Card front">
    <div class="brand">
      <span class="brand__dot"></span>
      <span class="brand__name">Quiet Renewal</span>
    </div>
  </section>

  <section class="card card--back" aria-label="Card back">
    <div class="brand">
      <span class="brand__dot"></span>
      <span class="brand__name">Quiet Renewal</span>
    </div>

    <div class="identity">
      <span class="identity__name">Mara Linden</span>
      <span class="identity__creds">Dip, Cert.</span>
      <span class="identity__rule"></span>
      <span class="identity__role">Kinesiologist</span>
    </div>

    <div class="contacts">
      <div class="contact">
        <svg class="contact__icon" viewBox="0 0 22 22" aria-hidden="true">
          <circle cx="11" cy="11" r="11" fill="var(--accent-orange)"/>
          <path d="M6 9.5c0-1.5 2.2-2.5 5-2.5s5 1 5 2.5v1h-2.4v-1.3h-5.2v1.3H6z" fill="#fff"/>
          <rect x="7" y="11.3" width="8" height="4.2" rx="1" fill="#fff"/>
        </svg>
        <span>0412 555 307</span>
      </div>
      <div class="contact">
        <svg class="contact__icon" viewBox="0 0 22 22" aria-hidden="true">
          <circle cx="11" cy="11" r="11" fill="var(--accent-orange)"/>
          <rect x="5.5" y="7" width="11" height="8" rx="0.8" fill="#fff"/>
          <path d="M5.8 7.4 11 11.6l5.2-4.2" fill="none" stroke="var(--accent-orange)" stroke-width="1.1"/>
        </svg>
        <span>maralinden@mail.com</span>
      </div>
    </div>
  </section>
</main>
</body>
</html>
```